A wine Label for a new brand of New Zealand Wine

We are looking for a Wine Label for our "Harbor Crest" brand of wines from North Otago New Zealand. We would like the label to perhaps use the HC as a logo and the rest up to the designer. We have our vineyards located in the Waitaki Valley New Zealand which is a southern region with mountains and a river flowing past our vineyard. Photos attached of Dramatic Landscape. Also attached is a basic outline of requirements for the front bottle of the label. The rear bottle label will contain writing about the wines background plus statutory regulations on Alc. Vol, bar code etc. Front Label size to be no Larger than 80mm deep by 100 mm wide. The label can be simple or graphic, whatever the designer chooses.
Target Market(s)
New Wine Brand
Look and feel
Each slider illustrates characteristics of the customer's brand and the style your logo design should communicate.

```html
<!DOCTYPE html>
<html lang="en">
<head>
<meta charset="utf-8">
<title>Harbor Crest – Pionts Gris 2015 Label</title>
<link rel="stylesheet" href="https://fonts.googleapis.com/css2?family=Playfair+Display:wght@400;600&family=Cormorant+Garamond:ital,wght@0,500;1,500&display=swap">
<style>
  :root {
    --backdrop: #3b2618;
    --paper: #efe3c4;
    --paper-edge: #e2cfa2;
    --gold: #b8934f;
    --ink-brown: #5e3a17;
    --vintage-red: #c2492a;
    --scene-light: #d9c49a;
    --scene-dark: #7a5426;
  }
  * { margin: 0; padding: 0; box-sizing: border-box; }
  html, body {
    width: 1110px;
    height: 1200px;
    overflow: hidden;
    background: var(--backdrop);
  }
  .canvas {
    position: relative;
    width: 1110px;
    height: 1200px;
  }
  .label {
    position: absolute;
    left: 193px;
    top: 53px;
    width: 724px;
    height: 1094px;
    background: radial-gradient(ellipse at 50% 45%, var(--paper) 60%, var(--paper-edge) 100%);
    color: var(--ink-brown);
    text-align: center;
  }
  .label__frame-outer,
  .label__frame-inner {
    position: absolute;
    border: 2px solid var(--gold);
    pointer-events: none;
  }
  .label__frame-outer { inset: 12px; border-width: 3px; }
  .label__frame-inner { inset: 24px; }
  .monogram {
    position: absolute;
    left: 50%;
    top: 90px;
    width: 112px;
    height: 112px;
    margin-left: -56px;
    border: 3px solid var(--gold);
    display: flex;
    align-items: center;
    justify-content: center;
    font-family: "Playfair Display", serif;
    font-weight: 400;
    font-size: 56px;
    color: var(--gold);
  }
  .brand-name {
    position: absolute;
    left: 0;
    right: 0;
    top: 240px;
    font-family: "Playfair Display", serif;
    font-weight: 600;
    font-size: 92px;
    line-height: 1;
    letter-spacing: -1px;
  }
  .landscape {
    position: absolute;
    left: 60px;
    top: 418px;
    width: 604px;
    height: 298px;
    background: linear-gradient(180deg, var(--paper) 0%, var(--scene-light) 30%, var(--scene-dark) 55%, var(--scene-light) 80%, var(--paper) 100%);
  }
  .varietal {
    position: absolute;
    left: 0;
    right: 0;
    top: 738px;
    font-family: "Playfair Display", serif;
    font-weight: 600;
    font-size: 82px;
    line-height: 1;
    letter-spacing: 1px;
  }
  .varietal-rule {
    position: absolute;
    left: 105px;
    right: 105px;
    top: 836px;
    height: 3px;
    background: var(--ink-brown);
  }
  .vintage {
    position: absolute;
    left: 0;
    right: 0;
    top: 862px;
    font-family: "Playfair Display", serif;
    font-weight: 400;
    font-size: 50px;
    line-height: 1;
    color: var(--vintage-red);
  }
  .region {
    position: absolute;
    left: 0;
    right: 0;
    top: 952px;
    font-family: "Cormorant Garamond", serif;
    font-style: italic;
    font-weight: 500;
    font-size: 34px;
    line-height: 1;
    color: #3a2a1a;
  }
  .origin {
    position: absolute;
    left: 0;
    right: 0;
    top: 1008px;
    font-family: "Cormorant Garamond", serif;
    font-weight: 500;
    font-size: 32px;
    line-height: 1;
    color: #3a2a1a;
  }
</style>
</head>
<body>
<div class="canvas">
  <section class="label">
    <div class="label__frame-outer"></div>
    <div class="label__frame-inner"></div>
    <div class="monogram">HC</div>
    <h1 class="brand-name">Harbor Crest</h1>
    <div class="landscape" role="img" aria-label="Sepia engraving of the vineyard with rolling hills and a mountain peak behind"></div>
    <h2 class="varietal">PIONTS GRIS</h2>
    <div class="varietal-rule"></div>
    <p class="vintage">2015</p>
    <p class="region">Waitaki Valley - North Otago</p>
    <p class="origin">New Zealand Wine</p>
  </section>
</div>
</body>
</html>
```